Sale of South Sea and Tahitian Pearl Jewellery, online business

I need a business card designed for my website business. We sell South Sea and Tahitian Pearl Jewellery. The colour theme for the website is black and white and would like to carry this through to business cards. Our brand is very elegant and stylish, would like sketch picture of women or fashion involving pearls if not the sketched picture then have the card very plan. below are pictures of the ideas I like and also the logo and writing that is used on my jewellery boxes.
Font is English Hand DB

Target Market(s)

30 and over women in the high end of the market

Industry/Entity Type

Business

Contact Information for Business Card

Business name - Varno Gems( front of card)
Back of card -Details
Rosalind Thackery
Gemmologist MDRS
email: rosalind@varnogems.com.au
website: varnogems.com.au
mob: +61 427 508 193
Perth Australia

Varno Stelle PTY T/AS Varno Gems
ABN 47 283 915 604

Colors
1b1b1b
ffffff
85cae6

Requirements
Must have
• Black and white colour preferably black card with white writing and picture.
• The Same writing as logo and writing on box packaging, attached a file with writing.
• Business name on one side of the card and all other details on the other side.
• Can have tiny hints of the harbour blue colour.
• Font: English Hand DB
Nice to have
• I really like the idea of having a sketch of a stylish or elegent lady wearing pearls or a sketch of a pearl, if not the sketch a really plain and simple card.
Should not have
• busy patterns.

```html
<!DOCTYPE html>
<html lang="en">
<head>
<meta charset="utf-8">
<title>Varno Gems — Business Cards</title>
<link href="https://fonts.googleapis.com/css2?family=Montserrat:wght@400;600&display=swap" rel="stylesheet">
<style>
  :root {
    --ink: #1b1b1b;
    --ink-soft: #3a3a3a;
    --paper: #ffffff;
    --stage: #e9e7e4;
    --rule: #2a2a2a;
    --sketch-light: #f2f2f2;
    --sketch-mid: #b9b9b9;
    --sketch-dark: #2b2b2b;
  }
  * { margin: 0; padding: 0; box-sizing: border-box; }
  html, body {
    width: 1200px; height: 913px; overflow: hidden;
    background: var(--stage);
    font-family: "Montserrat", sans-serif;
    color: var(--ink);
  }
  .canvas { position: relative; width: 1200px; height: 913px; }
  .card {
    position: absolute;
    width: 540px; height: 309px;
    background: var(--paper);
    border-radius: 16px;
    box-shadow: 0 6px 18px rgba(0,0,0,.18);
    overflow: hidden;
  }
  .card--details { left: 50px; top: 110px; }
  .card--brand { left: 610px; top: 490px; }

  /* details side */
  .monogram {
    position: absolute; left: 62px; top: 86px;
    width: 138px; height: 138px;
    border: 2px solid var(--ink); border-radius: 50%;
    display: flex; align-items: center; justify-content: center;
    font-size: 17px; font-weight: 400; color: var(--ink);
  }
  .divider {
    position: absolute; left: 246px; top: 70px;
    width: 1px; height: 170px; background: var(--rule);
  }
  .contact { position: absolute; left: 272px; top: 70px; }
  .contact__name { font-size: 18px; font-weight: 600; }
  .contact__title { font-size: 12px; color: var(--ink-soft); margin-top: 3px; }
  .contact__city { font-size: 12px; color: var(--ink-soft); margin-top: 22px; }
  .contact__list { list-style: none; margin-top: 16px; }
  .contact__list li {
    display: flex; align-items: center; gap: 8px;
    font-size: 12px; line-height: 19px; color: var(--ink-soft);
  }
  .contact__list svg { width: 10px; height: 10px; flex: none; }

  /* brand side */
  .fashion-sketch {
    position: absolute; left: 0; top: 40px;
    width: 250px; height: 269px;
    background: linear-gradient(160deg, var(--sketch-light) 0%, var(--sketch-mid) 45%, var(--sketch-dark) 100%);
  }
  .brand-name {
    position: absolute; right: 36px; top: 80px;
    font-size: 40px; font-weight: 400; color: var(--ink);
  }
  .legal {
    position: absolute; right: 36px; top: 190px;
    text-align: right; font-size: 12px; line-height: 19px; color: var(--ink-soft);
  }
</style>
</head>
<body>
<main class="canvas">

  <section class="card card--details" aria-label="Card back with contact details">
    <div class="monogram">Varno Gems</div>
    <div class="divider"></div>
    <div class="contact">
      <p class="contact__name">Rosalind Thackery</p>
      <p class="contact__title">Gemmologist MDRS</p>
      <p class="contact__city">Perth Australia</p>
      <ul class="contact__list">
        <li>
          <svg viewBox="0 0 10 10"><rect x="2.5" y="0.5" width="5" height="9" rx="1" fill="none" stroke="currentColor"/></svg>
          +61 427 508 193
        </li>
        <li>
          <svg viewBox="0 0 10 10"><rect x="0.5" y="2" width="9" height="6" fill="none" stroke="currentColor"/><path d="M0.5 2 L5 5.5 L9.5 2" fill="none" stroke="currentColor"/></svg>
          rosalind@varnogems.com.au
        </li>
        <li>
          <svg viewBox="0 0 10 10"><circle cx="5" cy="5" r="4.5" fill="none" stroke="currentColor"/><path d="M0.5 5 H9.5 M5 0.5 C2.5 3 2.5 7 5 9.5 M5 0.5 C7.5 3 7.5 7 5 9.5" fill="none" stroke="currentColor" stroke-width=".8"/></svg>
          www.varnogems.com.au
        </li>
      </ul>
    </div>
  </section>

  <section class="card card--brand" aria-label="Card front with business name">
    <div class="fashion-sketch" role="img" aria-label="Fashion sketch of an elegant woman in a black dress wearing long strands of pearls"></div>
    <p class="brand-name">Varno Gems</p>
    <p class="legal">Varno Stelle PTY T/AS Varno Gems<br>ABN 47 283 915 604</p>
  </section>

</main>
</body>
</html>
```